Quorenta - Automated robotic Inspection with AI need new business cards

We need a new design of our business cards. The company is focused on automated quality control at high speed with unmatched results. We have a logo but need a more forward leaning business card that shows that we are delivering cutting edge technology.

Contact Information for Business Card

Name
Position
Adress
Phone
Email
e.g.
Lotta Berglund
Chief Financial Officer (CFO)

Quorenta Sweden AB
Rönnvägen 14, SE-175 43 JÄRFÄLLA, Sweden
Mobile: +46701 23 45 67 | Office: +46 8 52 61 74
www.quorenta-example.com

Font styles to use
Sans Serif

```html
<!DOCTYPE html>
<html lang="en">
<head>
<meta charset="utf-8">
<title>Quorenta – Business Card</title>
<link rel="stylesheet" href="https://fonts.googleapis.com/css2?family=Arimo:wght@400;700&family=Exo+2:wght@700&display=swap">
<style>
  :root {
    --page-bg: #000000;
    --card-bg: #333438;
    --card-bg-dark: #2b2c30;
    --text-light: #ffffff;
    --text-soft: #e6e6e8;
    --divider: #6a6b70;
    --brand-blue: #1f5b8e;
  }
  * { margin: 0; padding: 0; box-sizing: border-box; }
  html, body {
    width: 1200px; height: 900px; overflow: hidden;
    background: var(--page-bg);
    font-family: "Arimo", Arial, sans-serif;
  }
  .canvas { position: relative; width: 1200px; height: 900px; }
  .card {
    position: absolute;
    width: 458px; height: 281px;
    border-radius: 13px;
    background:
      repeating-linear-gradient(90deg, rgba(255,255,255,0.018) 0 1px, rgba(0,0,0,0.02) 1px 3px),
      linear-gradient(180deg, var(--card-bg) 0%, var(--card-bg-dark) 100%);
    overflow: hidden;
  }
  .card--front { left: 137px; top: 265px; }
  .card--back { left: 625px; top: 268px; }

  .wordmark {
    position: absolute;
    display: flex; align-items: center; gap: 8px;
    font-family: "Arimo", Arial, sans-serif;
    font-weight: 700;
    letter-spacing: 0.02em;
  }
  .wordmark__dot { border-radius: 50%; flex: none; }
  .card--front .wordmark {
    left: 29px; top: 122px;
    font-size: 31px; color: var(--text-light);
  }
  .card--front .wordmark__dot { width: 16px; height: 16px; background: var(--text-light); }
  .card--back .wordmark {
    left: 0; right: 0; top: 108px; justify-content: center; gap: 14px;
    font-size: 54px; color: var(--brand-blue);
  }
  .card--back .wordmark__dot { width: 28px; height: 28px; background: var(--brand-blue); }

  .divider {
    position: absolute; left: 236px; top: 61px;
    width: 1px; height: 160px; background: var(--divider);
  }
  .details {
    position: absolute; left: 251px; top: 57px;
    color: var(--text-soft); font-size: 14px; line-height: 16.5px;
  }
  .details__name {
    font-family: "Exo 2", "Arimo", sans-serif;
    font-weight: 700; font-size: 18px; line-height: 20px;
    color: var(--text-light); letter-spacing: 0.01em;
  }
  .details__title { margin-bottom: 9px; }
  .contact-list { list-style: none; margin-bottom: 10px; }
  .contact-list li { display: flex; align-items: center; gap: 6px; }
  .contact-list svg { width: 11px; height: 11px; flex: none; }
  .details__company { font-weight: 700; color: var(--text-light); }
</style>
</head>
<body>
<main class="canvas">
  <section class="card card--front" aria-label="Business card front">
    <div class="wordmark"><span class="wordmark__dot"></span>QUORENTA</div>
    <div class="divider"></div>
    <div class="details">
      <p class="details__name">LOTTA BERGLUND</p>
      <p class="details__title">Chief Financial Officer (CFO)</p>
      <ul class="contact-list">
        <li>
          <svg viewBox="0 0 12 12" aria-hidden="true"><rect x="2.5" y="0.8" width="7" height="10.4" rx="1" fill="none" stroke="#fff" stroke-width="1.2"/><rect x="5" y="8.8" width="2" height="1" fill="#fff"/></svg>
          +46701 23 45 67
        </li>
        <li>
          <svg viewBox="0 0 12 12" aria-hidden="true"><path d="M2.2 1.2l2 .3.8 2.4-1.2.9c.6 1.4 1.6 2.4 3 3l.9-1.2 2.4.8.3 2-1.4 1.2C5 10.2 1.8 7 1 2.6z" fill="none" stroke="#fff" stroke-width="1.1"/></svg>
          +46 8 52 61 74
        </li>
        <li>
          <svg viewBox="0 0 12 12" aria-hidden="true"><rect x="0.8" y="2.3" width="10.4" height="7.4" fill="none" stroke="#fff" stroke-width="1.1"/><path d="M0.8 2.3L6 6.6l5.2-4.3" fill="none" stroke="#fff" stroke-width="1.1"/></svg>
          info@quorenta-example.com
        </li>
        <li>
          <svg viewBox="0 0 12 12" aria-hidden="true"><g fill="none" stroke="#fff" stroke-width="1"><circle cx="6" cy="6" r="5"/><ellipse cx="6" cy="6" rx="2.2" ry="5"/><path d="M1 6h10M1.8 3.5h8.4M1.8 8.5h8.4"/></g></svg>
          www.quorenta-example.com
        </li>
      </ul>
      <p class="details__company">QUORENTA SWEDEN AB</p>
      <p>Rönnvägen 14, SE-175 43</p>
      <p>JÄRFÄLLA, Sweden</p>
    </div>
  </section>

  <section class="card card--back" aria-label="Business card back">
    <div class="wordmark"><span class="wordmark__dot"></span>QUORENTA</div>
  </section>
</main>
</body>
</html>
```